Covid 19 Exit Strategy one page brochure

I would like to design, and will need URGENT help, a brochure detailing a Covid 19 Exit Strategy plan. This brochure will need to be understood easily and the graphics inside should make it easy for people to understand without reading the entire text. This project is quite urgent and needs to be completed THIS WEEK - by Saturday may 16th at the latest. I am attaching two examples. I will provide the text.

```html
<!DOCTYPE html>
<html lang="en">
<head>
<meta charset="utf-8">
<title>Covid 19 Phased Exit Strategy</title>
<link href="https://fonts.googleapis.com/css2?family=Oswald:wght@500;600;700&family=Roboto+Condensed:wght@400;700&family=Nunito+Sans:wght@400;600&display=swap" rel="stylesheet">
<style>
:root{
  --page:#e9eaec;
  --navy:#1c3f82;
  --navy-deep:#16336c;
  --blue:#2a62b4;
  --sky:#4ea2de;
  --sky-soft:#6cb4e6;
  --pale:#e4f1fb;
  --pale-2:#cfe6f6;
  --red:#e1252b;
  --ink:#5a6b82;
  --white:#ffffff;
}
*{box-sizing:border-box;margin:0;padding:0}
html,body{width:1200px;height:3643px;overflow:hidden;background:var(--page)}
body{font-family:"Roboto Condensed",sans-serif;color:var(--ink)}
.sheet{position:absolute;left:197px;top:222px;width:765px;box-shadow:0 2px 10px rgba(0,0,0,.25);background:var(--white)}
.hero{position:relative;height:461px;background:radial-gradient(circle at 75% 30%,#2f66b8 0%,var(--navy) 55%,var(--navy-deep) 100%);color:var(--white);padding:44px 40px 0}
.hero h1{font-family:"Oswald",sans-serif;font-weight:700;line-height:1.08;font-size:56px;letter-spacing:.5px}
.hero h1 .tag{color:var(--red);display:block}
.hero .byline{font-family:"Nunito Sans",sans-serif;font-size:17px;margin-top:8px}
.hero .map{position:absolute;left:369px;top:33px;width:373px;height:240px;border-radius:40px 70px 50px 90px;background:radial-gradient(circle at 50% 45%,#ffffff 0%,#dbe8f6 60%,rgba(120,170,230,.3) 100%)}
.hero .intro{position:absolute;left:40px;right:40px;top:312px;font-family:"Nunito Sans",sans-serif;font-size:12.2px;line-height:1.45;color:#dbe6f6;text-align:justify}
.general{height:392px;background:linear-gradient(135deg,#fff 40%,var(--pale) 100%);padding:16px 40px 0}
.general h2{font-family:"Oswald",sans-serif;font-weight:600;font-size:18px;color:var(--navy);text-align:center;margin-bottom:18px}
.reqs{display:grid;grid-template-columns:1fr 1fr;column-gap:40px}
.reqs ul{list-style:none}
.reqs li{position:relative;padding-left:20px;font-size:12px;line-height:1.3;margin-bottom:16px;text-align:justify}
.reqs li::before{content:"";position:absolute;left:0;top:2px;width:10px;height:10px;border:1.5px solid var(--navy);border-radius:2px}
.reqs li::after{content:"";position:absolute;left:3px;top:3px;width:4px;height:7px;border:solid var(--navy);border-width:0 2px 2px 0;transform:rotate(45deg)}
.stage-head{background:var(--navy);color:var(--white);padding:16px 40px 0;height:97px}
.stage-head.tall{height:105px}
.stage-title{display:flex;align-items:center;margin-left:-40px;margin-bottom:12px}
.stage-title .num{background:var(--red);font-family:"Oswald",sans-serif;font-weight:600;font-size:17px;padding:2px 14px 2px 40px;margin-right:14px}
.stage-title .name{font-family:"Oswald",sans-serif;font-weight:500;font-size:17px}
.stage-head p{font-size:12.8px;line-height:1.3}
.rows{position:relative}
.row{position:relative;height:85px}
.rows.short .row{height:83px}
.cell{position:absolute;top:0;height:100%;width:54%;display:flex;align-items:center;font-size:11.6px;line-height:1.2}
.cell.l{left:0;clip-path:polygon(0 0,100% 0,88% 100%,0 100%);padding-left:50px;padding-right:90px}
.cell.r{right:0;clip-path:polygon(12% 0,100% 0,100% 100%,0 100%);padding-left:70px;padding-right:80px}
.cell .ico{position:absolute;width:48px;height:48px;top:50%;margin-top:-24px}
.cell.l .ico{left:0}
.cell.r .ico{right:20px}
.t-on-blue{color:var(--white)}
.t-on-pale{color:var(--ink)}
.bg-sky{background:var(--sky)}
.bg-blue{background:var(--blue)}.bg-navy{background:var(--navy)}
.bg-white{background:#fff}.bg-pale{background:var(--pale)}.bg-pale2{background:var(--pale-2)}
.ico-blue{fill:var(--blue)}.ico-white{fill:#fff}
.band{display:flex;align-items:center;justify-content:center;text-align:center;padding:0 44px;font-size:12px;line-height:1.25;height:98px;color:var(--white)}
.band.s1{background:var(--sky)}
.band.s2{background:var(--blue);height:99px}
.band.s3{background:var(--navy);height:99px}
.footer{height:85px;text-align:center;padding-top:22px;background:#fff}
.footer .plan{font-family:"Oswald",sans-serif;font-weight:600;color:var(--red);font-size:16px}
.footer .by{font-family:"Nunito Sans",sans-serif;color:var(--blue);font-size:18px}
</style>
</head>
<body>
<svg width="0" height="0" style="position:absolute">
  <defs>
    <symbol id="i-house" viewBox="0 0 48 48"><path d="M24 4 4 22h6v22h28V22h6z"/></symbol>
    <symbol id="i-people" viewBox="0 0 48 48"><circle cx="10" cy="10" r="5"/><circle cx="24" cy="10" r="5"/><circle cx="38" cy="10" r="5"/><rect x="5" y="17" width="10" height="26" rx="3"/><rect x="19" y="17" width="10" height="26" rx="3"/><rect x="33" y="17" width="10" height="26" rx="3"/></symbol>
    <symbol id="i-distance" viewBox="0 0 48 48"><circle cx="8" cy="10" r="5"/><circle cx="40" cy="10" r="5"/><rect x="3" y="17" width="10" height="27" rx="3"/><rect x="35" y="17" width="10" height="27" rx="3"/><rect x="15" y="22" width="18" height="2"/></symbol>
    <symbol id="i-car" viewBox="0 0 48 48"><path d="M6 22 12 12h24l6 10h4v14H2V22z"/><circle cx="12" cy="38" r="4"/><circle cx="36" cy="38" r="4"/></symbol>
    <symbol id="i-building" viewBox="0 0 48 48"><rect x="8" y="14" width="14" height="32"/><rect x="24" y="4" width="16" height="42"/></symbol>
    <symbol id="i-group" viewBox="0 0 48 48"><circle cx="12" cy="16" r="6"/><circle cx="36" cy="16" r="6"/><circle cx="24" cy="22" r="6"/><path d="M2 36c0-8 20-8 20 0zM26 36c0-8 20-8 20 0zM12 44c0-9 24-9 24 0z"/></symbol>
    <symbol id="i-shop" viewBox="0 0 48 48"><rect x="4" y="4" width="40" height="8"/><path d="M6 14h36v32H6zm4 4v24h10V18zm16 0v12h12V18z"/></symbol>
    <symbol id="i-cross" viewBox="0 0 48 48"><rect x="22" y="4" width="4" height="40"/><path d="M4 12c8 0 12 4 18 6v4C14 20 8 18 4 12zM44 12c-8 0-12 4-18 6v4c8-2 14-4 18-10z"/><circle cx="24" cy="6" r="3"/></symbol>
    <symbol id="i-church" viewBox="0 0 48 48"><rect x="22" y="2" width="4" height="10"/><rect x="19" y="5" width="10" height="3"/><path d="M24 12 12 24v22h24V24zM2 30h10v16H2zM36 30h10v16H36z"/></symbol>
    <symbol id="i-hotel" viewBox="0 0 48 48"><rect x="4" y="16" width="16" height="30"/><rect x="24" y="4" width="20" height="42"/></symbol>
    <symbol id="i-cafe" viewBox="0 0 48 48"><rect x="4" y="6" width="40" height="10" rx="2"/><rect x="6" y="20" width="36" height="4"/><rect x="8" y="24" width="3" height="20"/><rect x="37" y="24" width="3" height="20"/><rect x="18" y="30" width="12" height="3"/></symbol>
    <symbol id="i-book" viewBox="0 0 48 48"><path d="M4 8c8-2 14 0 19 4v30c-5-4-11-6-19-4zM44 8c-8-2-14 0-19 4v30c5-4 11-6 19-4z"/></symbol>
    <symbol id="i-cal" viewBox="0 0 48 48"><path d="M4 8h40v38H4zm4 10v24h32V18z"/><rect x="12" y="22" width="5" height="5"/><rect x="21" y="22" width="5" height="5"/><rect x="30" y="22" width="5" height="5"/><rect x="12" y="31" width="5" height="5"/><rect x="21" y="31" width="5" height="5"/><rect x="30" y="31" width="5" height="5"/></symbol>
    <symbol id="i-hospital" viewBox="0 0 48 48"><rect x="6" y="4" width="4" height="12"/><rect x="2" y="8" width="12" height="4"/><rect x="16" y="14" width="14" height="32"/><rect x="30" y="4" width="14" height="42"/></symbol>
    <symbol id="i-mask" viewBox="0 0 48 48"><path d="M24 4c-11 0-18 8-18 18 0 6 3 10 6 13v11h16v-6h6c3 0 4-2 4-5v-6h4l-4-8c0-10-5-17-14-17z" fill="none" stroke="currentColor" stroke-width="2.5"/></symbol>
  </defs>
</svg>

<main class="sheet">
  <header class="hero">
    <h1><span class="tag">COVID 19</span>PHASED EXIT<br>STRATEGY</h1>
    <p class="byline">Developed by Lena Haddad</p>
    <div class="map" role="img" aria-label="Illustration of a map of the United States covered with virus particles"></div>
    <p class="intro">Pandemics have, historically, seen their end both medically - via herd immunity or immunitions. And while there are several clinical trials underway for potential Covid-19 vaccines, we are still a long way from deploying an effective vaccine and one that will stand the test of time as the virus changes. Covid-19 pandemic will be considered 'ended' when there are only occasional traces of localized cases that are quickly contained in specific locations. Today and in the absence of an effective vaccine(s) and for the re-opening of the economies and social activities to be successful, it is critical that the following basic conditions be in place before any lockdowns are lifted and before social activities resume:</p>
  </header>

  <section class="general">
    <h2>GENERAL REQUIREMENTS:</h2>
    <div class="reqs">
      <ul>
        <li>Single digit downward trend of documented cases within the past 14-days.</li>
        <li>Hospitals and the health care system are capable of treating patients without operating on a crisis mode.</li>
        <li>Ability to screen and test symptomatic individuals within 24 hours of identification. Increased and sufficient testing capacity, to test at least 50% of all population if necessary within a timeframe of 3 months.</li>
        <li>Ability to surge ICU capacity on a short notice - 24h.</li>
        <li>Ability to track and trace infected patients and contacts on a live basis and across the country and ability to react quickly to any unusual trends or outbreaks.</li>
      </ul>
      <ul>
        <li>Plan in place to trigger targeted or full-scale containment in case of sudden outbreaks.</li>
        <li>Mandatory use of masks (at least surgical grade) for everyone in all public areas and at work. Mandatory use of N95, or equivalent, masks for all healthcare front workers and for all government agencies and authorities that are involved in overseeing the containment activities.</li>
        <li>Mandatory daily checks of body temperature for everyone at the workplace or entering public areas.</li>
        <li>Mandatory sanitation in all places - use of disinfection available on a large scale.</li>
      </ul>
    </div>
  </section>

  <section class="stage-head">
    <div class="stage-title"><span class="num">STAGE 1:</span><span class="name">PHASED COVID-19 LOCKDOWN EXIT STRATEGY PLAN</span></div>
    <p>To enter this stage, additional to the general requirements, the Effective Reproduction Number (Rt) must be less than 1 and the death rate at less than 3%. The economy and social activities can resume in this sequence:</p>
  </section>
  <div class="rows">
    <div class="row bg-sky">
      <div class="cell l bg-sky t-on-blue"><svg class="ico ico-white" style="left:50px"><use href="#i-house"/></svg><span class="txt" style="margin-left:60px">Elderly (60+ years old) and vulnerable individuals should continue to self-isolate.</span></div>
      <div class="cell r bg-white t-on-pale"><span class="txt">Non-essential travel should be minimized between cities and regions (and within cities and regions where covid-19 infections are still a risk)</span><svg class="ico ico-blue"><use href="#i-car"/></svg></div>
    </div>
    <div class="row bg-sky">
      <div class="cell l bg-sky t-on-blue"><svg class="ico ico-white" style="left:50px"><use href="#i-people"/></svg><span class="txt" style="margin-left:60px">No more than 5 people maximum gathering at a time in public areas and at work.</span></div>
      <div class="cell r bg-white t-on-pale"><span class="txt">Large businesses (300 people and more) can reopen progressively. Common areas should remain closed (cafeteria, restaurant, gym, meeting rooms of no more than 5 people).</span><svg class="ico ico-blue"><use href="#i-building"/></svg></div>
    </div>
    <div class="row bg-sky">
      <div class="cell l bg-sky t-on-blue"><svg class="ico ico-white" style="left:50px"><use href="#i-house"/></svg><span class="txt" style="margin-left:60px">Work from home should continue whenever and as much as possible.</span></div>
      <div class="cell r bg-pale t-on-pale"><span class="txt">Small businesses (300 people and less) can reopen as well with the same conditions as large businesses.</span><svg class="ico ico-blue"><use href="#i-group"/></svg></div>
    </div>
    <div class="row bg-sky">
      <div class="cell l bg-sky t-on-blue"><svg class="ico ico-white" style="left:50px"><use href="#i-distance"/></svg><span class="txt" style="margin-left:60px">Social distancing should continue to be re-enforced in public areas, at work and in all areas reopened.</span></div>
      <div class="cell r bg-pale2 t-on-pale"><span class="txt">Commercial shops can reopen. Shops should control the flow of people in their facilities not to exceed 30% at a time of standard capacity.</span><svg class="ico ico-blue"><use href="#i-shop"/></svg></div>
    </div>
  </div>
  <div class="band s1">Transportation (buses, taxis, airlines) will resume progressively. No air travels permitted in and out of Covid-19 known hotspots, locally or internationally. Entry to country should be limited and strictly controlled. All landing passengers and visitors regardless of the country of origin should be tested for Covid-19 at arrival. All passengers and visitors will undergo a temperature check at arrival. No more than 3 people at a time in a taxi/rideshare including the driver. All passengers wearing masks. Buses should operate with no more than 30% customer's capacity per bus.</div>
  <div class="rows short">
    <div class="row bg-sky">
      <div class="cell l bg-white t-on-pale"><svg class="ico ico-blue" style="left:50px"><use href="#i-cross"/></svg><span class="txt" style="margin-left:60px">Pharmacies will continue to be open with limit the number of client/patient in their stores not to exceed 30% of the standard capacity.</span></div>
      <div class="cell r bg-sky t-on-blue"><span class="txt">Coffee &amp; restaurants can reopen but must operate at 30% capacity as well and comply with social distancing.</span><svg class="ico ico-white"><use href="#i-cafe"/></svg></div>
    </div>
    <div class="row bg-sky">
      <div class="cell l bg-white t-on-pale"><svg class="ico ico-blue" style="left:50px"><use href="#i-church"/></svg><span class="txt" style="margin-left:60px">Religious sites can reopen with a maximum capacity of 30% or less. Social distancing and wearing masks is mandatory.</span></div>
      <div class="cell r bg-sky t-on-blue"><span class="txt">All schools should remain closed. On-line courses should continue be the preferred method for education.</span><svg class="ico ico-white"><use href="#i-book"/></svg></div>
    </div>
    <div class="row bg-sky">
      <div class="cell l bg-pale t-on-pale"><svg class="ico ico-blue" style="left:50px"><use href="#i-hotel"/></svg><span class="txt" style="margin-left:60px">Hotels &amp; tourism (museums, etc.) can reopen but must operate at 30% or less capacity. All common areas should remain closed.</span></div>
      <div class="cell r bg-sky t-on-blue"><span class="txt">Large scale events (cinema, theaters, sport, business conferences, etc.) should remain closed or operate virtually.</span><svg class="ico ico-white"><use href="#i-cal"/></svg></div>
    </div>
  </div>

  <section class="stage-head tall">
    <div class="stage-title"><span class="num">STAGE 2:</span><span class="name">PHASED COVID-19 LOCKDOWN EXIT STRATEGY PLAN</span></div>
    <p>To enter stage 2 of the Covid-19 Exit Strategy, compliance to the general requirements is compulsory, additional to a successful Stage 1 outcome. The Effective Reproduction Number (Rt) for Stage 2 must be less than 0.5 and the death rate stabilized at less than 1.5%. The economy and social activities can resume in this sequence:</p>
  </section>
  <div class="rows">
    <div class="row bg-blue">
      <div class="cell l bg-blue t-on-blue"><svg class="ico ico-white" style="left:50px"><use href="#i-house"/></svg><span class="txt" style="margin-left:60px">Elderly (60+ years old) and vulnerable individuals should continue to self-isolate as much as possible.</span></div>
      <div class="cell r bg-white t-on-pale"><span class="txt">Travel can resume between cities and regions. The same containment restrictions should apply to any existing hotspot.</span><svg class="ico ico-blue"><use href="#i-car"/></svg></div>
    </div>
    <div class="row bg-blue">
      <div class="cell l bg-blue t-on-blue"><svg class="ico ico-white" style="left:50px"><use href="#i-people"/></svg><span class="txt" style="margin-left:60px">No more than 10 people maximum gathering at a time in public areas and at work.</span></div>
      <div class="cell r bg-white t-on-pale"><span class="txt">Elective surgeries can resume in hospitals and clinics that are equipped to comply with all general requirements.</span><svg class="ico ico-blue"><use href="#i-hospital"/></svg></div>
    </div>
    <div class="row bg-blue">
      <div class="cell l bg-blue t-on-blue"><svg class="ico ico-white" style="left:50px"><use href="#i-house"/></svg><span class="txt" style="margin-left:60px">Work from home should if possible or for jobs that do not have to be necessarily in an office setup.</span></div>
      <div class="cell r bg-pale t-on-pale"><span class="txt">Large businesses (300 people and more, manufacturing, services, etc.) will continue to operate.</span><svg class="ico ico-blue"><use href="#i-group"/></svg></div>
    </div>
    <div class="row bg-blue">
      <div class="cell l bg-blue t-on-blue"><svg class="ico" style="left:50px;color:#fff"><use href="#i-mask"/></svg><span class="txt" style="margin-left:60px">Social distancing can be relaxed. However people should continue to wear masks and use disinfectants.</span></div>
      <div class="cell r bg-pale2 t-on-pale"><span class="txt">Commercial shops will continue to be open and can operate at 50% capacity. Wear of masks should continue.</span><svg class="ico ico-blue"><use href="#i-shop"/></svg></div>
    </div>
  </div>
  <div class="band s2">Transportation (buses, taxis, and airlines) will continue to operate. Still no air travels permitted in and out of Covid-19 known hotspots, locally or internationally. Entry to country should be limited but remain controlled. Airports should continue to use thermo cameras to monitor passenger's temperature at landing. Airports should be equipped to test for Covid-19 if necessary. Transportation by taxi/rideshare continues, however, passengers wear masks. Buses could operate with 50% capacity per bus.</div>
  <div class="rows short">
    <div class="row bg-blue">
      <div class="cell l bg-white t-on-pale"><svg class="ico ico-blue" style="left:50px"><use href="#i-cross"/></svg><span class="txt" style="margin-left:60px">Pharmacies will continue to be open and will need to operate a 50% capacity.</span></div>
      <div class="cell r bg-blue t-on-blue"><span class="txt">Coffee &amp; restaurants can operate at 50% capacity and continue comply with social distancing. Clients must wear as much as possible their masks.</span><svg class="ico ico-white"><use href="#i-cafe"/></svg></div>
    </div>
    <div class="row bg-blue">
      <div class="cell l bg-white t-on-pale"><svg class="ico ico-blue" style="left:50px"><use href="#i-church"/></svg><span class="txt" style="margin-left:60px">Religious sites can operate with a maximum capacity of 50%. Social distancing and wearing masks should be enforced.</span></div>
      <div class="cell r bg-blue t-on-blue"><span class="txt">Schools can reopen in parallel with on-line education. Social distancing and re-arranging school seating to prevent the spread of infection is mandatory.</span><svg class="ico ico-white"><use href="#i-book"/></svg></div>
    </div>
    <div class="row bg-blue">
      <div class="cell l bg-pale t-on-pale"><svg class="ico ico-blue" style="left:50px"><use href="#i-hotel"/></svg><span class="txt" style="margin-left:60px">Hotels &amp; tourism (museums, etc.) can operate at 50% capacity. All common areas (restaurants, gyms, swimming pools,) could reopen.</span></div>
      <div class="cell r bg-blue t-on-blue"><span class="txt">Large scale events (cinema, theaters, sport, business conferences, etc.) could resume under strict social distancing. People should wear masks.</span><svg class="ico ico-white"><use href="#i-cal"/></svg></div>
    </div>
  </div>

  <section class="stage-head tall">
    <div class="stage-title"><span class="num">STAGE 3:</span><span class="name">PHASED COVID-19 LOCKDOWN EXIT STRATEGY PLAN</span></div>
    <p>To enter stage 3 of the Covid-19 Exit Strategy, compliance to the general requirements is compulsory, additional to a successful Stage 2 outcome. The Effective Reproduction Number (Rt) for Stage 3 must be less than 0.3 and the death rate stabilized at less than 1%. The economy and social activities can resume in this sequence:</p>
  </section>
  <div class="rows">
    <div class="row bg-navy" style="height:87px">
      <div class="cell l bg-navy t-on-blue"><svg class="ico ico-white" style="left:50px"><use href="#i-people"/></svg><span class="txt" style="margin-left:60px">Elderly (60+ years old) and vulnerable individuals may resume all previously exercised activities without restrictions.</span></div>
      <div class="cell r bg-white t-on-pale"><span class="txt">All hospital and clinic surgeries can resume in hospitals in compliance with standard hospital and health care procedures.</span><svg class="ico ico-blue"><use href="#i-hospital"/></svg></div>
    </div>
    <div class="row bg-navy" style="height:87px">
      <div class="cell l bg-navy t-on-blue"><svg class="ico ico-white" style="left:50px"><use href="#i-people"/></svg><span class="txt" style="margin-left:60px">Restrictions as to the number of people gathering together can be lifted. Social distancing can be relaxed. However, wear of masks may continue.</span></div>
      <div class="cell r bg-pale t-on-pale"><span class="txt">Large businesses (300 people and more, manufacturing, services, etc.) will resume normal business practices. Wear of masks is recommended but not mandatory.</span><svg class="ico ico-blue"><use href="#i-group"/></svg></div>
    </div>
    <div class="row bg-navy" style="height:88px">
      <div class="cell l bg-navy t-on-blue"><svg class="ico ico-white" style="left:50px"><use href="#i-car"/></svg><span class="txt" style="margin-left:60px">Travel can resume between cities and regions and out of country travel. The same containment restrictions as Stage 1 and 2 would continue.</span></div>
      <div class="cell r bg-pale2 t-on-pale"><span class="txt">Commercial shops can operate on a normal mode - previous to covid-19. Wear of masks could be recommended in certain areas.</span><svg class="ico ico-blue"><use href="#i-shop"/></svg></div>
    </div>
  </div>
  <div class="band s3">Transportation (buses, taxis, and airlines) will operate at a normal capacity. Still no air travels permitted in and out of Covid-19 known hotspots, locally or internationally. Entry to country should be relaxed and operate normally. Airports should continue to use thermo cameras to monitor passenger's temperature at landing. Airports should be equipped to test for Covid-19 if necessary. Transportation by taxi/rideshare and buses will resume on a normal mode. Wear of masks is elective.</div>
  <div class="rows short">
    <div class="row bg-navy" style="height:83px">
      <div class="cell l bg-white t-on-pale"><svg class="ico ico-blue" style="left:50px"><use href="#i-cross"/></svg><span class="txt" style="margin-left:60px">Pharmacies can operate at a normal state.</span></div>
      <div class="cell r bg-navy t-on-blue"><span class="txt">Coffee &amp; restaurants can resume normal operations. Clients may wear masks for personal protection if they wish to.</span><svg class="ico ico-white"><use href="#i-cafe"/></svg></div>
    </div>
    <div class="row bg-navy" style="height:83px">
      <div class="cell l bg-white t-on-pale"><svg class="ico ico-blue" style="left:50px"><use href="#i-church"/></svg><span class="txt" style="margin-left:60px">Religious sites can operate normally. Wear of masks should be elective.</span></div>
      <div class="cell r bg-navy t-on-blue"><span class="txt">Schools can resume operations. Re-arranging school seating should continue until a vaccine is found.</span><svg class="ico ico-white"><use href="#i-book"/></svg></div>
    </div>
    <div class="row bg-navy" style="height:82px">
      <div class="cell l bg-pale t-on-pale"><svg class="ico ico-blue" style="left:50px"><use href="#i-hotel"/></svg><span class="txt" style="margin-left:60px">Hotels &amp; tourism (museums, etc.) can operate at 100% capacity including all common areas.</span></div>
      <div class="cell r bg-navy t-on-blue"><span class="txt">Large scale events (cinema, theaters, sport, business conferences, etc.) could resume under moderate social distancing. People may elect to wear masks.</span><svg class="ico ico-white"><use href="#i-cal"/></svg></div>
    </div>
  </div>

  <footer class="footer">
    <div class="plan">PHASED COVID-19 LOCKDOWN EXIT STRATEGY PLAN</div>
    <div class="by">Developed by Lena Haddad</div>
  </footer>
</main>
</body>
</html>
```